Harbinger Noble Alloys Works Business Cards

We are wanting to have a new business card designed for our company as we go to a convention. We want to balance business/Modern with elegance and beauty. Our company sells highend jewelry pieces. We want to utilize the colors of Black and Gold and have gold foiled fonts to be physically printed on the business cards.
We also would like to have space to write notes on the back side of the business card. When we meet people at jewelry conventions we would like to write notes if possible.
Here are websites and designs that we like the look and feel of these companies and you can use these as design ideas.
https://www.lorvanne.com
https://www.bellquist.com/en-us/home
Here is our company website link
www.harbingernaw.com
I also up loaded two versions of our logo.
- Update 4.26.22
I have uploaded photos of a business card we like. this card has raised embossed letters that you can feel. the raise letters are like a plastic but we don't need to use that...I uploaded to show you that we like the experience of the client feeling the characters of the logo. we also would like to have the material as a satin or some material very soft.
- Maybe we can get designs with beautiful gold foiling and raised characters and logos. we like simplicity...not busy but an elegant design. We need to write notes and would like a section where we can write notes. but we want an elegant style and the client has an experience with the feel of the card when they touch the card.
Colors
- Main colors Black & Gold
- white or light colors for small notes section.
Specialty ideals and things we would like to see based on your design styles.
- raised fonts
- raised logos
- gold foiling
- satin/soft finish on the card material.
we are wanting to design a business card that looks elegant and clean. When the client is handed the business card we want them to physically experience the business card as well by touching the raised logos or fonts and the base material is soft satin. I hope this helps with further designs.
thank you all
We uploaded a new contact layout that we have designed in our office. we would like to see how this would look on your designs.
thank you
I just finished uploading the Contact Layout. the colors are just examples. please use this layout as an idea and use colors based on the feed back we have given each of you personally.
Contact Information for Business Card
we need an area to write notes, we would like to have our logos or the diamond of our logo or the business card to have embossed sections to the business card so when the customer touches the card they can feel the logo. we would also like sections of our business card to have gold foiling. we would also like to use a satin soft paper with our card. when the client touches the card its super soft and high quality
Requirements
Must have
- we would like to have our logos or the diamond of our logo or the business card to have embossed sections to the business card so when the customer touches the card they can feel the logo. we would also like sections of our business card to have gold foiling. we would also like to use a satin soft paper with our card. when the client touches the card its super soft and high quality
Nice to have
- we would like to have our logos or the diamond of our logo or the business card to have embossed sections to the business card so when the customer touches the card they can feel the logo. we would also like sections of our business card to have gold foiling.

```html
<!DOCTYPE html>
<html lang="en">
<head>
<meta charset="utf-8">
<title>Harbinger Noble Alloys — Business Card</title>
<link href="https://fonts.googleapis.com/css2?family=Cinzel:wght@400;500&display=swap" rel="stylesheet">
<style>
  :root {
    --backdrop: #55585c;
    --card-navy: #1f2c48;
    --card-navy-deep: #18233b;
    --foil-copper: #c98a68;
    --foil-silver: #e9e6e4;
  }
  * { margin: 0; padding: 0; box-sizing: border-box; }
  html, body {
    width: 1200px;
    height: 736px;
    overflow: hidden;
    background: var(--backdrop);
  }
  .canvas {
    position: relative;
    width: 1200px;
    height: 736px;
    display: flex;
    align-items: center;
    justify-content: center;
  }
  .business-card {
    position: relative;
    width: 1000px;
    height: 572px;
    background: linear-gradient(160deg, var(--card-navy) 0%, var(--card-navy-deep) 100%);
    font-family: "Cinzel", serif;
    box-shadow: 0 10px 30px rgba(0,0,0,0.35);
  }
  .brand {
    position: absolute;
    top: 150px;
    left: 0;
    width: 100%;
    text-align: center;
  }
  .brand-name {
    color: var(--foil-copper);
    font-size: 50px;
    font-weight: 400;
    letter-spacing: 1px;
    line-height: 1;
  }
  .brand-tagline {
    margin-top: 12px;
    color: var(--foil-silver);
    font-size: 26px;
    letter-spacing: 2px;
    display: flex;
    align-items: center;
    justify-content: center;
    gap: 14px;
  }
  .brand-tagline .rule {
    display: inline-block;
    width: 26px;
    height: 2px;
    background: var(--foil-silver);
  }
  .person {
    position: absolute;
    top: 380px;
    right: 520px;
    text-align: right;
  }
  .person-name {
    color: var(--foil-copper);
    font-size: 40px;
    letter-spacing: 1px;
    line-height: 1.1;
  }
  .person-title {
    color: var(--foil-copper);
    font-size: 20px;
    letter-spacing: 1px;
    margin-top: 2px;
  }
  .divider {
    position: absolute;
    top: 362px;
    left: 500px;
    width: 2px;
    height: 116px;
    background: var(--foil-silver);
  }
  .contact {
    position: absolute;
    top: 364px;
    left: 528px;
    list-style: none;
    color: var(--foil-silver);
    font-size: 21px;
    letter-spacing: 1px;
  }
  .contact li {
    display: flex;
    align-items: center;
    gap: 10px;
    height: 37px;
  }
  .contact svg {
    width: 16px;
    height: 16px;
    flex: none;
  }
</style>
</head>
<body>
<main class="canvas">
  <section class="business-card" aria-label="Business card front">
    <div class="brand">
      <h1 class="brand-name">Harbinger Noble Alloys</h1>
      <p class="brand-tagline"><span class="rule"></span>Coins, Jewelry &amp; Diamonds<span class="rule"></span></p>
    </div>

    <div class="person">
      <p class="person-name">Dorian Vale</p>
      <p class="person-title">CEO/Founder</p>
    </div>

    <div class="divider"></div>

    <ul class="contact">
      <li>
        <svg viewBox="0 0 16 16" aria-hidden="true"><path d="M4 1.5l2.2 3-1.4 1.6c.9 2 2.5 3.6 4.5 4.5l1.6-1.4 3 2.2-1.2 2.4C7.8 13.6 2.4 8.2 1.6 3z" fill="none" stroke="currentColor" stroke-width="1.3"/></svg>
        555-014-2290
      </li>
      <li>
        <svg viewBox="0 0 16 16" aria-hidden="true"><rect x="1.5" y="3.5" width="13" height="9" fill="none" stroke="currentColor" stroke-width="1.3"/><path d="M1.5 3.5L8 9l6.5-5.5" fill="none" stroke="currentColor" stroke-width="1.3"/></svg>
        info@harbingernaw.com
      </li>
      <li>
        <svg viewBox="0 0 16 16" aria-hidden="true"><circle cx="8" cy="8" r="6.5" fill="none" stroke="currentColor" stroke-width="1.2"/><ellipse cx="8" cy="8" rx="3" ry="6.5" fill="none" stroke="currentColor" stroke-width="1.1"/><path d="M1.5 8h13M2.5 4.8h11M2.5 11.2h11" stroke="currentColor" stroke-width="1"/></svg>
        www.harbingernaw.com
      </li>
    </ul>
  </section>
</main>
</body>
</html>
```